Birchmead Assurance Group Ltd needs a business card and logo

We need a logo for documents, invoices etc and a business card to match. We are a health auditing, training and consulting company based in NZ and working in both Australia and NZ. We ensure health organisations meet all their compliance requirements and develop expertise in the health auditing sector. The design should in some way reflect either symbols for quality management in the health sector.

Target Market(s)

Health providers and those wishing to increase their capability in meeting and understanding compliance requirements

Industry/Entity Type

Business

Contact Information for Business Card

Logo plus contact details

Logo Text

Health auditing, consultancy and training

Requirements
Must have
• Name and contact details director: Clara Hotham, chotham@bag-example.co.nz, PO Box 419, Warkworth, NZ, cell +6427390516

```html
<!DOCTYPE html>
<html lang="en">
<head>
<meta charset="utf-8">
<title>Clara Hotham – Business Card</title>
<link rel="stylesheet" href="https://fonts.googleapis.com/css2?family=Montserrat:wght@400;500&display=swap">
<style>
  :root {
    --paper: #ececec;
    --leaf-green: #84a723;
    --brand-blue: #0070bb;
    --name-olive: #6b8a1f;
    --white: #ffffff;
  }
  html, body {
    margin: 0;
    padding: 0;
    width: 1200px;
    height: 771px;
    overflow: hidden;
    background: var(--paper);
  }
  .card {
    position: relative;
    width: 1200px;
    height: 771px;
    background: var(--paper);
    font-family: "Montserrat", sans-serif;
    overflow: hidden;
  }
  .card-backdrop {
    position: absolute;
    inset: 0;
  }
  .brand-name {
    position: absolute;
    left: 120px;
    top: 474px;
    width: 300px;
    margin: 0;
    text-align: center;
    font-size: 36px;
    font-weight: 500;
    letter-spacing: 0.5px;
    color: var(--name-olive);
    white-space: nowrap;
  }
  .contact-list {
    position: absolute;
    left: 684px;
    top: 77px;
    margin: 0;
    padding: 0;
    list-style: none;
  }
  .contact-item {
    display: flex;
    align-items: center;
    height: 60px;
    margin-bottom: 16px;
  }
  .contact-icon {
    width: 55px;
    height: 60px;
    flex: none;
  }
  .contact-text {
    margin-left: 24px;
    font-size: 24px;
    font-weight: 400;
    letter-spacing: 1px;
    color: var(--white);
    white-space: nowrap;
  }
</style>
</head>
<body>
  <main class="card">
    <svg class="card-backdrop" viewBox="0 0 1200 771" width="1200" height="771" aria-hidden="true">
      <polygon class="green-panel" points="440,0 1200,0 1200,771 876,771" fill="var(--leaf-green)"/>
      <polygon class="blue-corner" points="657,771 1200,478 1200,771" fill="var(--brand-blue)"/>
    </svg>

    <p class="brand-name">CLARA HOTHAM</p>

    <ul class="contact-list">
      <li class="contact-item">
        <svg class="contact-icon" viewBox="0 0 55 60" aria-hidden="true">
          <polygon points="27.5,0 55,15 55,45 27.5,60 0,45 0,15" fill="var(--brand-blue)"/>
          <rect x="16" y="22" width="23" height="17" fill="var(--white)"/>
          <polyline points="16,22 27.5,32 39,22" fill="none" stroke="var(--brand-blue)" stroke-width="1.8"/>
          <polyline points="16,39 24,31 M39,39 31,31" fill="none" stroke="var(--brand-blue)" stroke-width="1.4"/>
        </svg>
        <span class="contact-text">chotham@bag-example.co.nz</span>
      </li>
      <li class="contact-item">
        <svg class="contact-icon" viewBox="0 0 55 60" aria-hidden="true">
          <polygon points="27.5,0 55,15 55,45 27.5,60 0,45 0,15" fill="var(--brand-blue)"/>
          <polygon points="27.5,18 41,30 38,30 38,41 31,41 31,34 24,34 24,41 17,41 17,30 14,30" fill="var(--white)"/>
        </svg>
        <span class="contact-text">PO Box 419, Warkworth,NZ</span>
      </li>
      <li class="contact-item">
        <svg class="contact-icon" viewBox="0 0 55 60" aria-hidden="true">
          <polygon points="27.5,0 55,15 55,45 27.5,60 0,45 0,15" fill="var(--brand-blue)"/>
          <path d="M20 19 l5 -1 l3 7 l-3 2 c1 4 4 7 8 8 l2 -3 l7 3 l-1 5 c-12 1 -22 -9 -21 -21 z" fill="var(--white)"/>
        </svg>
        <span class="contact-text">+6427390516</span>
      </li>
    </ul>
  </main>
</body>
</html>
```